MOSSGATE SPIRITWORKS WEBSITE

MOSSGATE SPIRITWORKS WHOLESALES ALCOHOL (WHISKY VODKA AND HELPS CREATES BOTTLING/BRANDING FOR PEOPLE WANTING LAUNCH THERE OWN BRANDS OF ALCOHOL

Colors

Designer to choose colors to be used in the design.

```html
<!DOCTYPE html>
<html lang="en">
<head>
<meta charset="utf-8">
<title>Mossgate Spiritworks – Contact</title>
<link rel="stylesheet" href="https://fonts.googleapis.com/css2?family=Sorts+Mill+Goudy&display=swap">
<style>
  :root {
    --ink: #111;
    --white: #fff;
    --gold: #d9b54f;
    --gold-line: #c9a23f;
    --footer-bg: #1e1a19;
    --hero-dark: #0d0906;
    --hero-mid: #3a2618;
    --hero-warm: #5b3d27;
  }
  * { box-sizing: border-box; margin: 0; padding: 0; }
  html, body { width: 1200px; height: 1153px; overflow: hidden; }
  body { position: relative; font-family: "Sorts Mill Goudy", Georgia, serif; color: var(--white); background: var(--footer-bg); }

  .hero-backdrop {
    position: absolute; left: 0; top: 0; width: 1200px; height: 884px;
    background:
      radial-gradient(ellipse 420px 320px at 760px 700px, rgba(120,80,50,.55), transparent 70%),
      radial-gradient(ellipse 300px 260px at 120px 720px, rgba(110,70,40,.5), transparent 70%),
      radial-gradient(ellipse 260px 380px at 300px 250px, rgba(70,45,30,.5), transparent 70%),
      linear-gradient(90deg, var(--hero-dark) 0%, var(--hero-mid) 45%, var(--hero-warm) 62%, var(--hero-dark) 100%);
  }

  .brand { position: absolute; display: flex; align-items: center; }
  .brand-dot { border-radius: 50%; background: var(--gold); }
  .brand-name { color: var(--white); letter-spacing: .08em; white-space: nowrap; }
  .site-header .brand { left: 34px; top: 29px; gap: 7px; }
  .site-header .brand-dot { width: 10px; height: 10px; }
  .site-header .brand-name { font-size: 11px; line-height: 1; }

  .main-nav a {
    position: absolute; top: 23px; height: 29px;
    display: flex; align-items: center; justify-content: center;
    border: 1px solid var(--white); color: var(--white);
    font-family: "Times New Roman", Times, serif; font-size: 11px; letter-spacing: .03em; text-decoration: none;
  }

  .page-title { position: absolute; left: 194px; top: 196px; font-size: 74px; font-weight: 400; line-height: 1; letter-spacing: .01em; }
  .title-rule { position: absolute; left: 194px; top: 287px; width: 121px; height: 1px; background: var(--gold-line); }

  .field {
    position: absolute; left: 194px; width: 396px; height: 43px;
    background: var(--white); border-radius: 3px;
    color: var(--ink); font-size: 21px; line-height: 43px; padding-left: 16px;
  }
  .field-message { left: 610px; top: 332px; height: 359px; line-height: 1; padding: 10px 14px; }
  .submit-button {
    position: absolute; left: 849px; top: 719px; width: 157px; height: 43px;
    background: var(--gold); border-radius: 3px; color: var(--ink);
    font-size: 21px; display: flex; align-items: center; justify-content: center;
  }

  .site-footer { position: absolute; left: 0; top: 884px; width: 1200px; height: 269px; background: var(--footer-bg); }
  .site-footer .brand { left: 155px; top: 78px; gap: 12px; }
  .site-footer .brand-dot { width: 26px; height: 26px; }
  .site-footer .brand-name { font-size: 25px; line-height: 1; }
  .footer-tagline { position: absolute; left: 158px; top: 168px; width: 300px; font-size: 15px; line-height: 19px; }
  .footer-divider { position: absolute; left: 600px; top: 50px; width: 1px; height: 162px; background: var(--white); }
  .contact-line { position: absolute; left: 730px; display: flex; gap: 11px; font-size: 20px; line-height: 25px; }
  .contact-line svg { flex: none; margin-top: 4px; }
  .contact-phone { top: 58px; }
  .contact-address { top: 107px; }
</style>
</head>
<body>
  <div class="hero-backdrop" role="img" aria-label="Dim distillery interior with oak barrels and a wooden door"></div>

  <header class="site-header">
    <div class="brand"><span class="brand-dot"></span><span class="brand-name">MOSSGATE SPIRITWORKS</span></div>
    <nav class="main-nav">
      <a href="#" style="left:367px;width:69px">HOME</a>
      <a href="#" style="left:482px;width:92px">WHOLESALE</a>
      <a href="#" style="left:624px;width:77px">SERVICES</a>
      <a href="#" style="left:751px;width:77px">CONTACT</a>
    </nav>
  </header>

  <main class="contact-section">
    <h1 class="page-title">Contact Us</h1>
    <div class="title-rule"></div>
    <div class="field" style="top:332px">First Name</div>
    <div class="field" style="top:395px">Last Name</div>
    <div class="field" style="top:458px">Company</div>
    <div class="field" style="top:521px">Email</div>
    <div class="field" style="top:584px">Telephone</div>
    <div class="field" style="top:647px">Website (optional)</div>
    <div class="field field-message">Type your message...</div>
    <div class="submit-button">Submit</div>
  </main>

  <footer class="site-footer">
    <div class="brand"><span class="brand-dot"></span><span class="brand-name">MOSSGATE SPIRITWORKS</span></div>
    <p class="footer-tagline">Turn your next drink idea into a reality and share your product with the world.</p>
    <div class="footer-divider"></div>
    <div class="contact-line contact-phone">
      <svg width="16" height="16" viewBox="0 0 24 24" fill="none" stroke="#d9b54f" stroke-width="2" stroke-linejoin="round"><path d="M5 3h4l2 5-2.5 1.5a11 11 0 0 0 6 6L16 13l5 2v4a2 2 0 0 1-2 2A16 16 0 0 1 3 5a2 2 0 0 1 2-2z"/></svg>
      <span>+31600481275</span>
    </div>
    <div class="contact-line contact-address">
      <svg width="16" height="18" viewBox="0 0 24 28" fill="none" stroke="#d9b54f" stroke-width="2"><path d="M12 26s9-8.5 9-15a9 9 0 0 0-18 0c0 6.5 9 15 9 15z"/><circle cx="12" cy="11" r="2.5" fill="#d9b54f" stroke="none"/></svg>
      <span>Mossgate Spiritworks Building 12,<br>Harbourline Estate, 4th<br>Quayside,<br>Westmere, 4410KD</span>
    </div>
  </footer>
</body>
</html>
```